Plumbing company needs a brochure design

Korvane Building Services is a mechanical services plumbing company that designs, installs, services and maintains commercial & industrial HVAC systems (heating, ventilation, air-conditioning systems manufactured by Trelbo, Fenwo and Halvoria Electric).
We would like a brochure that could be sent to prospects following a cold or warm call as a general introduction prior to a sales appointment.
We'd like to incorporate our 'breath clean air' campaign in the brochure as well. Details are on our website
The services we'd like to focus on the following services: Air conditioning; Design; Service & Maintenance; Air Filtration; and Refrigeration. No need to mention labour hire or trades & services
Our website is korvanebuildingservices.example
Target Market(s)
Building and property managers; building owners; facility managers of restaurants; hospitals; aged care facilities; conference centres; shopping centres
Industry/Entity Type
Industrial
Requirements
Must have
- 4 pages; contact details on last page (same as listed on our 'Contact Us' page on website. Half fold

```html
<!DOCTYPE html>
<html lang="en">
<head>
<meta charset="utf-8">
<title>Korvane Building Services – Brochure</title>
<link rel="stylesheet" href="https://fonts.googleapis.com/css2?family=Open+Sans:wght@400;600;700;800&family=Tinos:wght@400;700&display=swap">
<style>
  :root{
    --bg:#2b2b2b;
    --blue:#1b55a8;
    --blue-mid:#2463bd;
    --blue-deep:#0b2d6e;
    --orange:#f36b1c;
    --ink:#2a2a2a;
    --grey:#555b63;
    --paper:#ffffff;
    --mist:#eef1f5;
  }
  *{box-sizing:border-box;margin:0;padding:0}
  html,body{width:902px;height:1200px;overflow:hidden;background:var(--bg)}
  body{position:relative;font-family:"Open Sans",Arial,sans-serif;color:var(--ink)}
  .spread{position:absolute;left:31px;width:840px;height:546px;overflow:hidden;box-shadow:0 6px 18px rgba(0,0,0,.45)}
  .spread--outer{top:28px}
  .spread--inner{top:626px}
  .page{position:absolute;top:0;width:420px;height:546px;overflow:hidden}
  .page--left{left:0}
  .page--right{left:420px}
  .page-art{position:absolute;left:0;top:0;width:420px;height:546px}
  .abs{position:absolute}
  .hd{font-weight:800;text-transform:uppercase;letter-spacing:.2px;line-height:1}
  .hd .accent{color:var(--orange)}
  .dot-list{list-style:none}
  .dot-list li{position:relative;padding-left:12px}
  .dot-list li::before{content:"";position:absolute;left:0;top:.35em;width:6px;height:6px;border-radius:50%;background:var(--orange)}

  /* outer spread – back page */
  .back{background:var(--paper)}
  .about-title{left:22px;top:22px;font-size:19px;color:var(--blue-deep)}
  .about-intro{left:22px;top:46px;width:268px;font-size:7.6px;line-height:9.6px;color:var(--ink)}
  .about-building{left:298px;top:44px;width:102px;height:72px;background:linear-gradient(180deg,#9fb7d3 0%,#c9d3dd 45%,#8a8f96 100%);border:1px solid #ccc}
  .about-points{left:22px;top:128px;width:378px;font-size:7.6px;line-height:9.6px}
  .about-points li{margin-bottom:7px}
  .maker-row{left:40px;top:280px;display:flex;gap:48px;align-items:center}
  .maker{font-size:10px;font-weight:700;color:var(--blue-deep);display:flex;align-items:center;gap:5px}
  .maker .sq{width:8px;height:8px;background:var(--blue-deep)}
  .contact-title{left:22px;top:352px;font-size:16px;color:var(--paper)}
  .office{font-size:8.2px;line-height:10px;color:var(--paper)}
  .office b{display:flex;align-items:center;gap:4px;font-weight:700}
  .office .pin{width:8px;height:8px}
  .office p{padding-left:12px}
  .office--mel{left:22px;top:378px}
  .office--png{left:22px;top:432px}
  .office--per{left:152px;top:378px}
  .office--chn{left:152px;top:432px}
  .offer-tag{left:300px;top:372px;width:96px;height:130px;border:1.2px solid rgba(255,255,255,.85);border-radius:14px;color:var(--paper);text-align:center;padding:6px 6px 0}
  .offer-tag .ring{width:64px;height:64px;margin:0 auto;border:1.2px solid rgba(255,255,255,.85);border-radius:50%;display:flex;flex-direction:column;justify-content:center;font-size:5px;letter-spacing:.5px}
  .offer-tag .ring strong{font-size:9px;font-weight:600;line-height:10px;letter-spacing:0;margin:2px 0}
  .offer-tag .terms{font-size:6.4px;line-height:7.8px;margin-top:4px}
  .offer-tag .terms small{display:block;font-size:5px}
  .contact-foot{left:22px;top:514px;width:380px;display:flex;justify-content:space-between;font-size:8.4px;font-weight:700;color:var(--paper)}
  .contact-foot span{display:flex;align-items:center;gap:4px}
  .contact-foot svg{width:8px;height:8px}

  /* outer spread – cover */
  .cover{background:var(--paper)}
  .cover-call{left:34px;top:50px}
  .cover-call .lead{font-size:13px;font-weight:800;color:var(--orange);letter-spacing:.3px}
  .cover-call .num{font-size:21px;font-weight:700;color:var(--blue-deep);line-height:24px}
  .brand{right:16px;top:24px;display:flex;align-items:flex-start;gap:6px}
  .brand .sq{width:12px;height:12px;background:var(--blue)}
  .brand .name{font-size:10.5px;font-weight:800;line-height:12px;color:var(--blue);text-transform:uppercase;text-align:left}

  /* inner spread – left */
  .inside-left{background:var(--mist)}
  .services-title{left:20px;top:205px;font-size:19px;color:var(--paper)}
  .services-list{left:22px;top:233px;font-size:14px;font-weight:600;color:var(--paper);line-height:25px}
  .services-list li{padding-left:16px}
  .services-list li::before{width:10px;height:10px;top:8px}
  .trade-badge{left:22px;top:362px;width:140px;height:42px;background:var(--paper)}
  .know-title{left:214px;top:198px;font-size:18px;color:var(--ink)}
  .know-list{left:214px;top:224px;width:196px;list-style:none;font-size:7.3px;line-height:9px;color:var(--grey)}
  .know-list li{position:relative;padding-left:12px;margin-bottom:8px}
  .know-list svg{position:absolute;left:0;top:1px;width:8px;height:8px}
  .trade-title{left:214px;top:378px;width:196px;font-size:10px;color:var(--ink);border-bottom:1px solid #c5ccd6;padding-bottom:4px}
  .trade-list{left:214px;top:398px;width:196px;font-family:"Tinos","Times New Roman",serif;font-size:7.2px;line-height:8.6px;color:var(--grey)}
  .trade-list li{margin-bottom:4px;padding-left:8px}
  .trade-list li::before{width:3px;height:3px;background:var(--grey);top:.45em}

  /* inner spread – right */
  .inside-right{background:var(--paper)}
  .col-title{top:22px;font-size:15px;color:var(--paper)}
  .col-body{top:44px;width:185px;font-family:"Tinos","Times New Roman",serif;font-size:7.5px;line-height:9px;color:var(--paper)}
  .col-body p{margin-bottom:8px}
  .col-body .dot-list li{padding-left:8px;font-weight:700}
  .col-body .dot-list li::before{width:4px;height:4px;top:.4em}
  .col--filter{left:18px}
  .col--fridge{left:218px}
  .sm-title{left:18px;top:376px;font-size:14px;color:var(--paper)}
  .sm-body{left:18px;top:395px;width:392px;font-size:7.2px;line-height:9px;color:var(--paper)}
  .sm-body p{margin-bottom:3px}
  .sm-body li{margin-bottom:3px;padding-left:10px}
  .sm-body li::before{width:5px;height:5px}

  .foot-bar{bottom:0;height:30px;display:flex;align-items:center;font-size:11.5px;font-weight:700;color:var(--paper)}
  .foot-bar--left{left:0;width:420px;justify-content:flex-end;padding-right:14px;background:linear-gradient(90deg,var(--blue-deep) 0%,var(--blue) 100%)}
  .foot-bar--right{left:0;width:420px;padding-left:16px;background:linear-gradient(90deg,var(--blue) 0%,var(--blue-deep) 65%,#cfd9e8 100%)}
</style>
</head>
<body>

<!-- Outer spread: back page and cover -->
<section class="spread spread--outer">

  <article class="page page--left back">
    <svg class="page-art" viewBox="0 0 420 546" aria-hidden="true">
      <defs>
        <linearGradient id="backBlue" x1="0" y1="0" x2="0" y2="1">
          <stop offset="0" stop-color="#2463bd"/><stop offset="1" stop-color="#0b2d6e"/>
        </linearGradient>
      </defs>
      <path d="M0,322 C130,372 300,370 420,300 L420,546 L0,546 Z" fill="url(#backBlue)"/>
      <path d="M0,314 C130,364 300,362 420,292" fill="none" stroke="#f36b1c" stroke-width="6"/>
      <path d="M0,304 C130,354 300,352 420,282" fill="none" stroke="#ffffff" stroke-width="4"/>
    </svg>

    <h2 class="abs hd about-title">About <span class="accent">Us</span></h2>
    <p class="abs about-intro">Because we design and supply systems that cut our clients' costs by reducing energy consumption; and deliver sustainable solutions to prolong service life and minimise maintenance costs. Our systems can save 20-40 per cent of your climate related energy costs annually, and reduce your carbon emissions. We use our own in-house mechanical engineers to design energy efficient and sustainable systems:</p>
    <div class="abs about-building" role="img" aria-label="Photo of the company's office building"></div>
    <ul class="abs dot-list about-points">
      <li>Using our own engineers means we can reduce overall engineering and commissioning time =cost savings for client</li>
      <li>Korvane can identify the most cost effective &amp; efficient system for client application and budget meaning right size systems so they work as they should; more reliable equipment means it works when you need it; and client doesn't need to spend any more than they should for a quality HVAC solution</li>
      <li>Korvane Engineers are on hand to advise technicians, installers and service mechanics. They are just a phone call away for timely advice. This means less down time, the likely elimination of error and therefore reduced client costs</li>
      <li>Often installation jobs need fine tuning as the work progress from plans to actual installation. Our team of engineers can resolve issues almost immediately so work does not stop.</li>
    </ul>
    <div class="abs maker-row">
      <span class="maker"><span class="sq"></span>Fenwo</span>
      <span class="maker">Halvoria Electric</span>
      <span class="maker">Trelbo</span>
    </div>

    <h2 class="abs hd contact-title">Contact <span class="accent">Us</span></h2>
    <div class="abs office office--mel">
      <b><svg class="pin" viewBox="0 0 10 10"><path d="M5 0 10 5H8.5V10H1.5V5H0Z" fill="#f36b1c"/></svg>Melbourne, VIC</b>
      <p>12 Ardent St<br>Riverbank 3006<br>Melbourne, VIC</p>
    </div>
    <div class="abs office office--png">
      <b><svg class="pin" viewBox="0 0 10 10"><path d="M5 0 10 5H8.5V10H1.5V5H0Z" fill="#f36b1c"/></svg>Papua New Guinea</b>
      <p>Korvane Building Services (PNG)<br>Limited<br>Harbourline Building<br>Ground Floor<br>Kessel Street<br>Port Moresby, PNG</p>
    </div>
    <div class="abs office office--per">
      <b><svg class="pin" viewBox="0 0 10 10"><path d="M5 0 10 5H8.5V10H1.5V5H0Z" fill="#f36b1c"/></svg>Perth, WA</b>
      <p>27-29 Foundry Avenue<br>Marlow 6112<br>Perth, WA</p>
    </div>
    <div class="abs office office--chn">
      <b><svg class="pin" viewBox="0 0 10 10"><path d="M5 0 10 5H8.5V10H1.5V5H0Z" fill="#f36b1c"/></svg>China</b>
      <p>No. 318<br>Building 6<br>Lanting Court<br>Qiaoxin Road<br>Heyuan Town<br>Dongguan Guangdong CHINA</p>
    </div>
    <div class="abs offer-tag">
      <div class="ring">SPECIAL OFFER<strong>Breathe<br>Clean<br>Air</strong>SPECIAL OFFER</div>
      <p class="terms">Replace your filters with our energy saving CLARION filters &amp; receive up to $500 in free installation<small>Terms and Conditions apply</small></p>
    </div>
    <div class="abs contact-foot">
      <span><svg viewBox="0 0 10 10"><circle cx="5" cy="5" r="4" fill="#f36b1c"/></svg>korvanebuildingservices.example</span>
      <span><svg viewBox="0 0 10 10"><path d="M2 1 4 1 5 3.5 3.8 4.6Q5 6.5 6.4 6.2L7.5 5 10 6V8Q10 9.5 8 9.5 1 8.5 0.5 2 0.5 1 2 1Z" fill="#f36b1c"/></svg>1300 555 014</span>
      <span><svg viewBox="0 0 10 10"><rect x="1" y="3" width="8" height="6" rx="1" fill="#f36b1c"/><rect x="3" y="0.5" width="4" height="3" fill="#f36b1c"/></svg>+61 3 5550 0142</span>
    </div>
  </article>

  <article class="page page--right cover">
    <svg class="page-art" viewBox="0 0 420 546" aria-hidden="true">
      <defs>
        <linearGradient id="coverBlue" x1="0" y1="0" x2="1" y2="1">
          <stop offset="0" stop-color="#2463bd"/><stop offset="1" stop-color="#0b2d6e"/>
        </linearGradient>
        <linearGradient id="unitTone" x1="0" y1="0" x2="1" y2="1">
          <stop offset="0" stop-color="#d9d2b8"/><stop offset=".45" stop-color="#b9b6a6"/><stop offset="1" stop-color="#6f7377"/>
        </linearGradient>
        <path id="badgeTop" d="M103,190 A47,47 0 0 1 197,190"/>
        <path id="badgeBottom" d="M99,190 A51,51 0 0 0 201,190"/>
      </defs>
      <path d="M0,300 C70,330 120,430 150,546 L0,546 Z" fill="url(#coverBlue)"/>
      <path d="M0,292 C74,322 126,424 158,546" fill="none" stroke="#f36b1c" stroke-width="6"/>
      <path d="M0,282 C78,312 134,420 168,546" fill="none" stroke="#ffffff" stroke-width="4"/>
      <path d="M180,546 C146,420 156,250 234,172 C292,122 360,120 420,122 L420,546 Z" fill="url(#unitTone)" role="img" aria-label="Photo of a packaged rooftop air conditioning unit"/>
      <path d="M172,546 C136,412 148,240 228,162 C290,108 360,106 420,108" fill="none" stroke="#f36b1c" stroke-width="6"/>
      <g>
        <circle cx="150" cy="190" r="60" fill="#ffffff"/>
        <circle cx="150" cy="190" r="56" fill="#1b55a8"/>
        <circle cx="150" cy="190" r="40" fill="none" stroke="#ffffff" stroke-width="1"/>
        <text font-family="Open Sans, sans-serif" font-size="7.5" fill="#ffffff" letter-spacing="1"><textPath href="#badgeTop" startOffset="50%" text-anchor="middle">SPECIAL OFFER</textPath></text>
        <text font-family="Open Sans, sans-serif" font-size="7.5" fill="#ffffff" letter-spacing="1"><textPath href="#badgeBottom" startOffset="50%" text-anchor="middle" dominant-baseline="hanging">SPECIAL OFFER</textPath></text>
        <rect x="108" y="170" width="84" height="40" fill="#0b2d6e" opacity=".35"/>
        <text x="150" y="180" text-anchor="middle" font-family="Open Sans, sans-serif" font-size="12" fill="#ffffff">Breathe</text>
        <text x="150" y="194" text-anchor="middle" font-family="Open Sans, sans-serif" font-size="12" fill="#ffffff">Clean</text>
        <text x="150" y="208" text-anchor="middle" font-family="Open Sans, sans-serif" font-size="12" fill="#ffffff">Air</text>
      </g>
    </svg>

    <div class="abs cover-call">
      <p class="lead">CALL US TODAY</p>
      <p class="num">1300 555 014</p>
    </div>
    <div class="abs brand">
      <span class="sq"></span>
      <span class="name">Korvane<br>Building<br>Services</span>
    </div>
  </article>
</section>

<!-- Inner spread -->
<section class="spread spread--inner">

  <article class="page page--left inside-left">
    <svg class="page-art" viewBox="0 0 420 546" aria-hidden="true">
      <defs>
        <linearGradient id="innerBlue" x1="0" y1="0" x2="0" y2="1">
          <stop offset="0" stop-color="#2463bd"/><stop offset="1" stop-color="#0b2d6e"/>
        </linearGradient>
        <linearGradient id="workerTone" x1="0" y1="0" x2="1" y2="1">
          <stop offset="0" stop-color="#8d97a3"/><stop offset=".5" stop-color="#b7bcc1"/><stop offset="1" stop-color="#d8dadb"/>
        </linearGradient>
      </defs>
      <path d="M110,0 L420,0 L420,185 L240,185 C225,110 180,40 110,0 Z" fill="url(#workerTone)" role="img" aria-label="Photo of a technician checking refrigerant pressure gauges"/>
      <path d="M0,0 L100,0 C170,45 210,130 205,240 L205,546 L0,546 Z" fill="url(#innerBlue)"/>
      <path d="M100,0 C170,45 210,130 205,240 L205,546" fill="none" stroke="#f36b1c" stroke-width="4"/>
      <path d="M20,0 L110,90" stroke="#ffffff" stroke-width="10" opacity=".5"/>
      <path d="M48,0 L130,82" stroke="#f36b1c" stroke-width="6"/>
    </svg>

    <h2 class="abs hd services-title">Our <span class="accent">Services</span></h2>
    <ul class="abs dot-list services-list">
      <li>Air conditioning</li>
      <li>Design</li>
      <li>Service &amp; Maintenance</li>
      <li>Air Filtration</li>
      <li>Refrigeration</li>
    </ul>
    <div class="abs trade-badge" role="img" aria-label="Trade association membership badge"></div>

    <h2 class="abs hd know-title">Did you know?</h2>
    <ul class="abs know-list">
      <li><svg viewBox="0 0 10 10"><path d="M1 5 4 8 9 1" fill="none" stroke="#f36b1c" stroke-width="2"/></svg>HVAC typically accounts for between 25-50 per cent of the total energy costs for businesses and commercial buildings.</li>
      <li><svg viewBox="0 0 10 10"><path d="M1 5 4 8 9 1" fill="none" stroke="#f36b1c" stroke-width="2"/></svg>By reducing draughts via leaks, gaps and cracks, you may save up to 25 per cent of your heating and cooling costs.</li>
      <li><svg viewBox="0 0 10 10"><path d="M1 5 4 8 9 1" fill="none" stroke="#f36b1c" stroke-width="2"/></svg>In summer, increasing the temperature of your air conditioning system by 1°C may reduce energy consumption and your bill by around 10 per cent.</li>
      <li><svg viewBox="0 0 10 10"><path d="M1 5 4 8 9 1" fill="none" stroke="#f36b1c" stroke-width="2"/></svg>By keeping your HVAC system well maintained, you may save on air conditioning operating costs.</li>
    </ul>
    <h3 class="abs hd trade-title">Licensed Plumber Services:</h3>
    <ul class="abs dot-list trade-list">
      <li>Project Management</li>
      <li>In-house engineered designed air-conditioning and chiller systems</li>
      <li>Install and commission air conditioning and chillers</li>
      <li>Service and Maintenance of air-conditioning and chiller systems</li>
      <li>Hire portable air conditioner, portable sirocos, portable ac</li>
      <li>Air Filtration - supply and fit energy efficient &amp; independently European certified air filters</li>
    </ul>

    <div class="abs foot-bar foot-bar--left">www.korvanebuildingservices.example</div>
  </article>

  <article class="page page--right inside-right">
    <svg class="page-art" viewBox="0 0 420 546" aria-hidden="true">
      <defs>
        <linearGradient id="panelBlue" x1="0" y1="0" x2="1" y2="1">
          <stop offset="0" stop-color="#2463bd"/><stop offset="1" stop-color="#0b2d6e"/>
        </linearGradient>
        <linearGradient id="siteTone" x1="0" y1="0" x2="1" y2="1">
          <stop offset="0" stop-color="#a9b4bd"/><stop offset=".6" stop-color="#8b8679"/><stop offset="1" stop-color="#6c6a64"/>
        </linearGradient>
        <linearGradient id="plantTone" x1="0" y1="0" x2="1" y2="1">
          <stop offset="0" stop-color="#c8c2b4"/><stop offset=".5" stop-color="#9a9187"/><stop offset="1" stop-color="#5e5a55"/>
        </linearGradient>
      </defs>
      <rect x="0" y="150" width="162" height="230" fill="url(#siteTone)" role="img" aria-label="Photo of outdoor condenser units beside a building"/>
      <rect x="166" y="150" width="254" height="230" fill="url(#plantTone)" role="img" aria-label="Photo of ceiling ductwork during a fit-out"/>
      <path d="M0,0 L420,0 L420,150 C300,180 140,170 0,190 Z" fill="url(#panelBlue)"/>
      <path d="M0,190 C140,170 300,180 420,150" fill="none" stroke="#f36b1c" stroke-width="4"/>
      <path d="M0,375 C150,352 300,356 420,336 L420,546 L0,546 Z" fill="url(#panelBlue)"/>
      <path d="M0,368 C150,345 300,349 420,329" fill="none" stroke="#f36b1c" stroke-width="4"/>
      <path d="M0,362 C150,339 300,343 420,323" fill="none" stroke="#ffffff" stroke-width="3"/>
    </svg>

    <h2 class="abs hd col-title col--filter">Air <span class="accent">Filtration</span></h2>
    <div class="abs col-body col--filter">
      <p><b>You can rely on us to:</b></p>
      <ul class="dot-list" style="margin-bottom:8px">
        <li>Help you find the correct filter part for your system</li>
        <li>Help you troubleshoot your system</li>
        <li>Remind you when to change your filters</li>
        <li>Send you new filters when you need them</li>
        <li>Maintain your air quality and comfort</li>
      </ul>
      <p><b>Korvane Building Services are a Clarion Filters Authorised Dealer. We are the exclusive supplier of Clarion's laboratory tested and certified filters in Western Australia, Papua New Guinea and the Asia Pacific region.</b></p>
    </div>

    <h2 class="abs hd col-title col--fridge"><span class="accent">R</span>efrigeration</h2>
    <div class="abs col-body col--fridge">
      <p><b>Korvane Building Services is your first choice for Refrigeration Solutions and Servicing. Our experienced refrigeration mechanics are highly skilled and efficient.</b></p>
      <p><b>Korvane Building Services focus is on providing best life cycle cost solutions benefits both our customer and the environment. Our solutions can be used in applications including refrigeration, process cooling, process heating, IT cooling and HVAC</b></p>
    </div>

    <h2 class="abs hd sm-title">Service and <span class="accent">Maintenance</span></h2>
    <div class="abs sm-body">
      <p>Korvane can help building owners and managers optimise existing HVAC systems in order to reduce energy costs. Optimisation includes:</p>
      <ul class="dot-list">
        <li>The use of control systems to ensure that the right amount of air conditioning is provided when and where it is required</li>
        <li>Temperature controller thermostats to reduce demand and save energy</li>
        <li>Streamlined air distribution systems reduce the demand for fan power and HVAC unit capacity. This reduces running costs and improves indoor comfort. For example, an increase in a ducts cross sectional area by 15% will reduce the friction rate by 50%, reduce pressure drop contributed to by the ducts by 50%, reduce overall pressure drop by 40% and reduce fan energy consumption by around 15-20%</li>
        <li>Insulate ducts to prevent undesireable heat transfer</li>
      </ul>
    </div>

    <div class="abs foot-bar foot-bar--right">Call Us on 1300 555 014</div>
  </article>
</section>

</body>
</html>
```